依頼詳細
下記ブランドコンセプトに沿ったご提案をお願い致します。
プロトタイプを添付いたします。構成等、より優れていると思えるご提案がありましたら無視して頂いて構いません。
ブランドコンセプトは以下の通りです。

-- 以下、ブランドコンセプト
「自然が持つ美しさ」と「暮らす人の思い」を取り入れ『生活が楽しい住まい』を創ります
人々に永く愛されてきた天然素材を使用することで自然素材だけが持つ色や質感から確かな手触りと温もりを暮らす人に与え続けてくれます。新しいだけを追い過ぎず自然素材の持つ機能性を生かして自然の働きでしっかりと家を守る
それは流行に左右されない気品を保つ「素朴で美しい風合い」に仕上がります。

住む人のライフスタイルや好みをしっかりとお聞かせいただいた上で土地を生かし隣地環境と調和のある設計を企画し、その人らしい家を一緒に考えていきます。
それはその人がどんなふうに暮らしていきたいのかを一緒に考え、その地で永く暮らしていくイメージを膨らませ生活が楽しくなる様な空間を提案します。
-- 以上、ブランドコンセプト
サイトURL
http://morvatu.com/
ページ数
1ページ
希望イメージ
シンプル 複雑
単色 カラフル
暗い 明るい
日常 高級
遊び心 厳粛
未来的 伝統的
女性的 男性的
希望する色
納品ファイル
補足説明
トップページに関するプロトタイプを「トップページ.png」として添付しております。
また、素材として利用可能なものは下記dropboxリンクよりご利用ください。
https://www.filqeno-share.com/sh/7kdpqe31vmx02z/QWkrtyuu_pLmNnbvZxCdeRtYsUoPw?dl=0

■ 選んだ理由

全員が色使いやコンテンツの配置などを理由として同デザインを選択しました。
似通ったデザインの中でも全員の目を引く、魅力的な部分があったのだと考えます。

■ 提案者全員のお礼・コメント

今回は多くの皆様に貴重なお時間を使って頂きご提案頂きました事、大変うれしく思い感謝申し上げます。
複数名で選考を行いましたが、選考するメンバー全員でどれも素晴らしいデザインだよねと口をそろえて申しておりました。

本当にありがとうございました。

```html
<!DOCTYPE html>
<html lang="ja">
<head>
<meta charset="utf-8">
<title>Morvatu | 自然素材の家づくり</title>
<link rel="stylesheet" href="https://fonts.googleapis.com/css2?family=Noto+Sans+JP:wght@400;500;700&display=swap">
<style>
:root{
  --ink:#4a4440;
  --muted:#7d7670;
  --accent:#d98a2a;
  --accent-soft:#f3e3cc;
  --nav:#1e5a73;
  --nav-dark:#163f52;
  --nav-active:#e9f1f3;
  --line:#ddd6cc;
  --footer:#3b342d;
  --footer-text:#cfc6ba;
  --paper:#ffffff;
  --bg:#f4f1ec;
}
*{box-sizing:border-box;margin:0;padding:0}
html,body{width:1200px;height:2300px;overflow:hidden}
body{background:var(--bg);font-family:"Noto Sans JP",sans-serif;color:var(--ink);font-size:13px;line-height:1.8}
.page{width:1200px;height:2300px;position:relative;background:var(--paper);overflow:hidden}
.wrap{width:800px;margin:0 auto;position:relative}

.site-header{height:108px;position:relative}
.site-header .tagline{position:absolute;left:0;top:10px;font-size:11px;color:var(--muted)}
.brand{position:absolute;left:50%;top:26px;transform:translateX(-50%);display:flex;align-items:center;gap:10px}
.brand-mark{width:34px;height:34px;border:2px solid var(--accent);border-radius:50%}
.brand-name{font-size:26px;font-weight:500;color:var(--nav);letter-spacing:2px;line-height:1.2}
.contact{position:absolute;right:0;top:12px;text-align:right}
.contact .hours{font-size:10px;color:var(--muted)}
.contact .tel{display:flex;align-items:center;gap:6px;justify-content:flex-end;font-size:26px;font-weight:700;color:var(--nav);line-height:1.2}
.contact .mail-btn{display:inline-block;margin-top:4px;background:var(--accent);color:#fff;font-size:11px;padding:2px 12px}

.hero{height:372px;position:relative;background:linear-gradient(180deg,#8fb4d6 0%,#c9dbe9 45%,#e8e6e0 62%,#7f7a70 80%,#6a7d52 100%)}
.hero .slogan{position:absolute;left:0;right:0;top:22px;text-align:center;font-size:30px;color:#fff;letter-spacing:2px;text-shadow:0 1px 3px rgba(0,0,0,.3)}
.hero .dots{position:absolute;bottom:14px;left:50%;transform:translateX(-50%);display:flex;gap:8px}
.hero .dots span{width:9px;height:9px;border-radius:50%;background:rgba(255,255,255,.6)}
.hero .dots span.on{background:#fff}

.global-nav{background:var(--nav);border-bottom:4px solid var(--nav-dark);height:44px}
.global-nav ul{list-style:none;display:flex;width:800px;margin:0 auto}
.global-nav li{flex:1;text-align:center;color:#fff;font-size:13px;line-height:40px;border-right:1px solid rgba(255,255,255,.25)}
.global-nav li:first-child{border-left:1px solid rgba(255,255,255,.25)}
.global-nav li.active{background:var(--nav-active);color:var(--nav)}

.content{display:flex;gap:24px;padding-top:34px;align-items:flex-start}
.main-col{width:540px}
.side-col{width:236px}
.sec-title{font-size:20px;font-weight:500;color:var(--accent);border-bottom:1px solid var(--line);padding-bottom:4px;margin-bottom:14px;line-height:1.5}
.concept p{margin-bottom:10px;font-size:12.5px}
.more-btn{display:inline-block;background:var(--nav);color:#fff;font-size:11px;padding:3px 14px}
.more-row{text-align:right;margin-top:8px}

.works .item{margin-bottom:14px}
.works .thumb{height:110px;background:linear-gradient(160deg,#b9cbd9,#e7e4dd 55%,#8d9676)}
.works .item:nth-of-type(2) .thumb{background:linear-gradient(160deg,#c4d3df,#d8d2c6 55%,#7c7a6c)}
.works .item:nth-of-type(3) .thumb{background:linear-gradient(160deg,#a9bfd0,#ece8e0 60%,#938a79)}
.works .cap{font-size:11px;color:var(--muted)}

.row2{display:flex;gap:24px;margin-top:26px}
.making{width:240px}
.making p{font-size:12.5px;margin-bottom:10px}
.inquiry{width:276px}
.form{border:1px solid var(--line)}
.form .f{display:flex;border-bottom:1px solid var(--line);min-height:34px}
.form .f label{width:96px;background:var(--accent);color:#fff;font-size:11.5px;padding:6px 8px;line-height:1.6}
.form .f .in{flex:1;background:#fbf7f1}
.form .f.tall{min-height:92px}
.form .send{text-align:center;padding:10px 0}
.form .send span{display:inline-block;background:var(--nav);color:#fff;font-size:12px;padding:4px 30px}

.news{margin-top:30px}
.news .post{display:flex;gap:16px;padding:9px 0;border-bottom:1px dotted var(--line)}
.news .pic{width:110px;height:70px;background:linear-gradient(150deg,#bccbd6,#e4ddd1 60%,#8f8a74);flex:none}
.news .post:nth-of-type(2) .pic{background:linear-gradient(150deg,#d6ccbe,#a99a84)}
.news h3{font-size:14px;font-weight:500;color:var(--nav);line-height:1.6}
.news p{font-size:11.5px;color:var(--muted);line-height:1.6}

.social{margin-top:26px}
.social .label{font-size:14px;font-weight:700;color:var(--nav);margin-bottom:6px}
.social .box{border:1px solid var(--line);padding:12px}
.social .head{display:flex;gap:10px;align-items:center;margin-bottom:10px;font-size:12px}
.social .sq{width:38px;height:38px;background:var(--accent-soft)}
.social .faces{display:flex;gap:6px;flex-wrap:wrap}
.social .faces span{width:44px;height:44px;background:#e4ded5}

.totop{position:absolute;right:200px;top:2008px;background:var(--nav);color:#fff;font-size:10px;padding:2px 10px}

.site-footer{position:absolute;left:0;top:2040px;width:1200px;height:260px;background:var(--footer);color:var(--footer-text)}
.site-footer .wrap{height:260px}
.f-tel{position:absolute;left:0;top:44px;display:flex;align-items:center;gap:8px;font-size:26px;font-weight:700;color:#fff;line-height:1.2}
.f-mail{position:absolute;left:0;top:86px;background:var(--accent);color:#fff;font-size:11px;padding:2px 14px}
.f-addr{position:absolute;left:0;top:114px;font-size:10.5px}
.f-brand{position:absolute;right:0;top:40px;display:flex;align-items:center;gap:10px}
.f-brand .brand-name{color:#fff}
.f-links{position:absolute;left:260px;top:112px;font-size:10.5px;display:flex;gap:14px}
.copy{position:absolute;left:0;right:0;top:196px;text-align:center;font-size:10px;border-top:1px solid #564d44;padding-top:14px}
</style>
</head>
<body>
<div class="page">
  <header class="site-header wrap">
    <p class="tagline">長野県の自然素材の家づくり｜モルヴァトゥ</p>
    <div class="brand"><span class="brand-mark"></span><span class="brand-name">Morvatu</span></div>
    <div class="contact">
      <div class="hours">営業時間 9:00〜18:00 定休日 水曜日</div>
      <div class="tel"><svg width="20" height="20" viewBox="0 0 24 24"><path d="M6.6 10.8a15 15 0 0 0 6.6 6.6l2.2-2.2a1 1 0 0 1 1-.25 11.4 11.4 0 0 0 3.6.6 1 1 0 0 1 1 1V20a1 1 0 0 1-1 1A17 17 0 0 1 3 4a1 1 0 0 1 1-1h3.5a1 1 0 0 1 1 1c0 1.25.2 2.45.6 3.6a1 1 0 0 1-.25 1z" fill="#1e5a73"/></svg>0120-48-3917</div>
      <span class="mail-btn">メールでのお問い合わせ</span>
    </div>
  </header>

  <section class="hero" role="img" aria-label="ウッドデッキのある白い外壁の二階建て住宅と青空の写真">
    <p class="slogan">広いデッキが織り成す広いくつろぎ空間</p>
    <div class="dots"><span class="on"></span><span></span><span></span></div>
  </section>

  <nav class="global-nav">
    <ul>
      <li class="active">トップページ</li><li>家づくり</li><li>建築事例</li><li>お問い合わせ</li><li>会社概要</li><li>会社情報</li>
    </ul>
  </nav>

  <div class="wrap">
    <div class="content">
      <div class="main-col">
        <section class="concept">
          <h2 class="sec-title">ブランドコンセプト</h2>
          <p>「自然が持つ美しさ」と「暮らす人の思い」を取り入れ『生活が楽しい住まい』を創ります。</p>
          <p>人々に永く愛されてきた天然素材を使用することで自然素材だけが持つ色や質感から確かな手触りと温もりを暮らす人に与え続けてくれます。</p>
          <p>新しいだけを追い過ぎず自然素材の持つ機能性を生かして自然の働きでしっかりと家を守る。それは流行に左右されない気品を保つ「素朴で美しい風合い」に仕上がります。</p>
          <p>住む人のライフスタイルや好みをしっかりとお聞かせいただいた上で土地を生かし隣地環境と調和のある設計を企画し、その人らしい家を一緒に考えていきます。</p>
          <p>それはその人がどんなふうに暮らしていきたいのかを一緒に考え、その地で永く暮らしていくイメージを膨らませ生活が楽しくなる様な空間を提案します。</p>
        </section>

        <div class="row2">
          <section class="making">
            <h2 class="sec-title">モルヴァトゥの家づくり</h2>
            <p>「自然が持つ美しさ」と「暮らす人の思い」を取り入れ『生活が楽しい住まい』を創ります。</p>
            <p>人々に永く愛されてきた天然素材を使用し、確かな手触りと温もりを暮らす人に与え続けます。</p>
            <p>土地を生かし隣地環境と調和のある設計を企画し、その人らしい家を一緒に考えていきます。</p>
            <p>その地で永く暮らしていくイメージを膨らませ、生活が楽しくなる様な空間を提案します。</p>
          </section>
          <section class="inquiry">
            <h2 class="sec-title">お問い合わせ</h2>
            <div class="form">
              <div class="f"><label>お名前</label><div class="in"></div></div>
              <div class="f"><label>フリガナ</label><div class="in"></div></div>
              <div class="f"><label>電話番号</label><div class="in"></div></div>
              <div class="f"><label>メール</label><div class="in"></div></div>
              <div class="f"><label>ご住所</label><div class="in"></div></div>
              <div class="f"><label>ご用件</label><div class="in"></div></div>
              <div class="f tall"><label>お問い合わせ内容</label><div class="in"></div></div>
              <div class="send"><span>送信する</span></div>
            </div>
          </section>
        </div>

        <section class="news">
          <h2 class="sec-title">最新情報</h2>
          <div class="post"><div class="pic" role="img" aria-label="記事の写真"></div><div><h3>記事タイトル</h3><p>完成見学会を開催します。自然素材の心地よさをぜひ体感しにお越しください。ご予約お待ちしております。</p></div></div>
          <div class="post"><div class="pic" role="img" aria-label="記事の写真"></div><div><h3>記事タイトル</h3><p>新しい施工事例を追加しました。広いデッキのある住まいの様子をご覧ください。</p></div></div>
          <div class="post"><div class="pic" role="img" aria-label="記事の写真"></div><div><h3>記事タイトル</h3><p>夏季休業のお知らせです。期間中のお問い合わせは休み明けに順次対応いたします。</p></div></div>
          <div class="more-row"><span class="more-btn">最新情報一覧</span></div>
        </section>

        <section class="social">
          <p class="label">ソーシャル</p>
          <div class="box">
            <div class="head"><span class="sq"></span><span>モルヴァトゥ｜いいね！ 128人</span></div>
            <div class="faces"><span></span><span></span><span></span><span></span><span></span><span></span><span></span><span></span><span></span><span></span><span></span><span></span><span></span><span></span><span></span><span></span><span></span><span></span><span></span><span></span></div>
          </div>
        </section>
      </div>

      <aside class="side-col works">
        <h2 class="sec-title">建築事例</h2>
        <div class="item"><div class="thumb" role="img" aria-label="施工住宅の外観写真"></div><p class="cap">自然素材の家 伊那市 T様邸</p></div>
        <div class="item"><div class="thumb" role="img" aria-label="施工住宅の外観写真"></div><p class="cap">平屋の家 駒ヶ根市 K様邸</p></div>
        <div class="item"><div class="thumb" role="img" aria-label="施工住宅の外観写真"></div><p class="cap">二世帯の家 箕輪町 S様邸</p></div>
        <div class="more-row"><span class="more-btn">建築事例一覧</span></div>
      </aside>
    </div>
  </div>

  <span class="totop">ページ上部へ</span>

  <footer class="site-footer">
    <div class="wrap">
      <div class="f-tel"><svg width="20" height="20" viewBox="0 0 24 24"><path d="M6.6 10.8a15 15 0 0 0 6.6 6.6l2.2-2.2a1 1 0 0 1 1-.25 11.4 11.4 0 0 0 3.6.6 1 1 0 0 1 1 1V20a1 1 0 0 1-1 1A17 17 0 0 1 3 4a1 1 0 0 1 1-1h3.5a1 1 0 0 1 1 1c0 1.25.2 2.45.6 3.6a1 1 0 0 1-.25 1z" fill="#ffffff"/></svg>0120-48-3917</div>
      <span class="f-mail">メールでのお問い合わせ</span>
      <p class="f-addr">営業時間 9:00〜18:00 定休日 水曜日</p>
      <div class="f-links"><span>トップページ</span><span>家づくり</span><span>建築事例</span><span>お問い合わせ</span><span>会社概要</span><span>会社情報</span></div>
      <div class="f-brand"><span class="brand-mark"></span><span class="brand-name">Morvatu</span></div>
      <p class="copy">Copyright © Morvatu All Rights Reserved.</p>
    </div>
  </footer>
</div>
</body>
</html>
```